Men's Health Coaching Business - UK based

I am a UK based Health Coach who requires a clean Word Press 'lifestyle' design. The website will be a window to my services and is not intended to be a place to hang volumes of information off. It needs to be professional looking but with a hint of fun; easy/fun to navigate, intuitive and pleasing to the eye.

The site needs to be image/icon/video based to attract potential clients to my health coaching service. it should also encompass a creative/strong 'Call to Action' throughout the site - i.e. 'contact me'. I will only be using Facebook and LinkedIn for social media. Please also consider the colours of the beach/ocean and other lifestyle images I intend to you.

Images in your submission:

I am doing a photoshoot in July/Aug and so there is no need seek 'ideal images' as I will have a personal catalogue to choose from - examples along the lines of the above brief will be fine in your submission.

Good luck, I look forward to your submissions. Thank you.

Target Market(s)

My target audience is successful/professional men aged 30+ who are likely to lead busy lives, Dads, and enjoy hobbies/activities that keep them fit and healthy. They are probably cash-rich but time-poor - hence the clean, intuitive requirement for the site. I am also male who has a family. I require the site to have a slightly more masculine look/feel to it i.e. font, shapes etc. It must also compliment my logo coaching philosophy (see below).

Industry/Entity Type

Health

Font styles to use
Sans Serif

Colors

Designer to choose colors to be used in the design.

Requirements
Must have
• I have uploaded my logo for reference and inspiration and some images that are similar to the those that will be used throughout the site. The concept is below, but please feel free to employ your 'creative genius' to how it will operate/look/work; In broad terms, I require the following:
• 1 (Home Page): This will need to strongly convey the 'Why' to clients using my services by 1. showcasing who I am (My Story) through a Vimeo/Youtube; 2. showing results of previous clients through an eye-catching testimonials section; and 3. conveying to clients (as creatively as possible) the comprehensive approach of my coaching business; through the following elements (if this can be represented through an eye-catching graphic that chimes with my logo - even better):
• - Nutrition
• - Exercise
• - Mental well-being
• - Sleep - adequate/quality
• - Play - rest and recuperation
• - Sunlight - adequate
• - Plan, execute, review
• 2. 'My Philosophy' page: This will contain a number of paragraphs outlining to potential clients my guiding principles. The headings for each paragraph are:
• - I empathise - I'm a busy family man.
• - I choose my clients extremely carefully.
• - I guide, you decide.
• - I give it to you straight.
• - I give you the tools to change, build great health and see results.
• - If you don't fully commit, we'll part company.
• - I'm evidence-based and results driven.
• - I trust the numbers.
• - Consistency over perfection.
• - I take a comprehensive approach.
• - Guiding principles, not a prescriptive programme.
• - I will recommend some products - I don't sell them.
• - I use technology when it's complimentary.
• - Exercise is important but it's not the only factor.
• - I keep it simple for success.
• - I incorporate interventions that give you the biggest bang for your buck.
• - My guidance is designed to blend with your life.
• - I take a layered and progressive approach.
• - We'll have fun with the process.
• On the philosophy page, the images will be more atuned to preparing meals with the kids in the kitchen and images depicting other aspects of the key pillars such as Play - games with the kids, hobbies, activities or sports; rest and recuperation (reading, holidays etc); and using your brain.
• 3. The 'Investment' page (my prices page). This page needs to show three different packages: Bronze, Silver and Gold. An editable info-graph for ease of readability and showing what the client gets for each package/cost.
• Page 4. The 'Project You' Page. This page will show the client journey; ideally, icon/graphic driven, it should show a typical journey for a client, incorporating the following (taken from the Bronze Package) - please make this quick and fun to view:
• - Meet-up: coffee shop, telephone/video call.
• - Client completes e-Questionnaire.
• - Client records a 'typical week' in a journal.
• - Analyse/discuss e-Questionnaire with the client.
• - Analyse/discuss journal with the client.
• - Testing - Health Markers.
• - Testing - Body Composition Measurement.
• - Fitness Testing (if required) - tailored to sport/activity and preference.
• - Intervention Design and Refine.
• - Clients keep a journal of progress + supporting Meet/Video/telephone consultations.
• - 3-month: re-testing of Health Markers, Body Composition and Fitness.
• The Silver and Gold packages incorporate further testing and interventions as required.
• Page 5. The 'Exercise Sessions' page - VLOG. This page will hold a catalogue of home-based exercise films via Vimeo/Youtube for clients to use/refer to/follow anytime/anywhere. For each post/session I require a template that (as creatively as possible) can:
• - Hold a video;
• - Incorporate an editable info-graph that allows me to the following information fixed information.
• - Session title (header)
• - Exercise names (a maximum of 4 for each clip)
• Against each exercise I need to be able to show some or all of the following information - preferably icon/minimum words driven:
• - Intensity (i.e. low, medium, high, maximum)
• - Coaching points (be able to list of 4-5 key coaching points).
• - Safety points (to be able to list 4-5 key safety points).
• - Session goal (i.e. Strength, CV fitness; movement competency etc).
• - Session - Total time
• - Target heart rate during work (i.e. 150-160bpm)
• - Equipment options (i.e. bodyweight, kettle bell, power-bag, weighted bar, Olympic bar etc)
• - Sets.
• - Reps per set (i.e. 15 reps).
• - Duration per set (i.e. 30s).
• - Block sets (i.e. 3 x 3 sets)
• - Rest between sets (i.e. 30s)
• - Rest between block sets (i.e. 2 min)
• - Tempo (i.e. 2s-1s-3s)
• - Interval ratio (i.e. 30s work/10s rest)
• - Recover heart rate target (i.e. 120bpm)
• Viewable on other devices with no change in format.
Nice to have
• Whilst I need it to be professional, a little humour (design, quotes) would be great...
Should not have
• The look I definitely don't want - Bootcamp; gym/personal trainer; corporate; consultancy; feminine; flowery; fashion; cartoon; cluttered and confusing.

```html
<!DOCTYPE html>
<html lang="en">
<head>
<meta charset="utf-8">
<title>Rob Carver – Men's Health Coaching</title>
<link rel="stylesheet" href="https://fonts.googleapis.com/css2?family=Raleway:ital,wght@0,400;0,500;0,600;0,700;0,800;1,400&display=swap">
<style>
  :root {
    --accent: #12b4e2;
    --accent-dark: #0e9ac3;
    --ink: #3a3a3a;
    --ink-soft: #555;
    --muted: #6a6a6a;
    --band: #f0f0f0;
    --white: #ffffff;
    --line: #d6d6d6;
  }
  * { box-sizing: border-box; margin: 0; padding: 0; }
  html, body { width: 1200px; height: 2394px; overflow: hidden; }
  body { position: relative; background: var(--white); font-family: "Raleway", sans-serif; color: var(--ink); }

  /* Header */
  .site-header { position: absolute; left: 0; top: 0; width: 1200px; height: 115px; background: var(--white); }
  .brand { position: absolute; left: 72px; top: 18px; width: 112px; text-align: center; }
  .brand-mark { display: block; width: 40px; height: 40px; margin: 0 auto 6px; border: 2px solid var(--accent); border-radius: 50%; }
  .brand-name { display: block; font-size: 19px; font-weight: 600; letter-spacing: 1px; color: var(--ink); line-height: 1; }
  .brand-tag { display: block; font-size: 7px; font-weight: 600; letter-spacing: 2px; color: var(--ink); margin-top: 4px; }
  .main-nav a { position: absolute; top: 55px; font-size: 13px; font-weight: 700; color: var(--ink); text-decoration: none; letter-spacing: .2px; }
  .main-nav a.is-active { color: var(--accent); }
  .btn-contact { position: absolute; left: 975px; top: 40px; width: 152px; height: 43px; background: var(--accent); color: var(--white); font-size: 13px; font-weight: 700; line-height: 43px; text-align: center; text-decoration: none; letter-spacing: .5px; }

  /* Hero */
  .hero { position: absolute; left: 0; top: 115px; width: 1200px; height: 531px; overflow: hidden; }
  .hero-photo { position: absolute; inset: 0; background: linear-gradient(180deg, #a9b8c2 0%, #8ea3ae 24%, #c9b79c 45%, #b7a287 70%, #9a8a76 100%); }
  .hero-curve { position: absolute; left: 0; bottom: 0; width: 1200px; height: 40px; }
  .hero-title { position: absolute; left: 0; top: 200px; width: 1200px; text-align: center; color: var(--white); font-size: 64px; font-weight: 700; line-height: 1; }
  .hero-sub { position: absolute; left: 0; top: 272px; width: 1200px; text-align: center; color: var(--white); font-size: 26px; font-weight: 700; }
  .hero-dots { position: absolute; left: 563px; top: 491px; display: flex; gap: 8px; }
  .hero-dots span { width: 12px; height: 12px; border-radius: 50%; background: var(--white); }
  .hero-dots span.is-current { background: var(--accent); }

  /* Section headings */
  .section-title { position: absolute; left: 0; width: 1200px; text-align: center; font-size: 27px; font-weight: 600; color: var(--ink); letter-spacing: .5px; }

  /* Pillars */
  .pillars-lead { position: absolute; left: 0; top: 762px; width: 1200px; text-align: center; font-size: 15px; color: var(--ink-soft); }
  .pillar { position: absolute; width: 260px; margin-left: -130px; text-align: center; }
  .pillar svg { display: block; margin: 0 auto; }
  .pillar-label { display: block; margin-top: 14px; font-size: 14px; font-weight: 700; letter-spacing: .3px; color: var(--ink); }

  /* Who I am */
  .about { position: absolute; left: 0; top: 1183px; width: 1200px; height: 488px; background: var(--band); }
  .about-video { position: absolute; left: 318px; top: 105px; width: 566px; height: 318px; background: linear-gradient(180deg, #7d8791 0%, #8e959b 45%, #747d86 62%, #5b6670 100%); }
  .play-btn { position: absolute; left: 253px; top: 128px; }

  /* Testimonials */
  .quote-card { position: absolute; top: 1776px; width: 331px; height: 192px; background: var(--accent); color: var(--white); padding: 18px 22px 0; text-align: center; font-size: 14px; font-style: italic; line-height: 24px; }
  .quote-avatar { position: absolute; top: 1922px; width: 92px; height: 92px; border-radius: 50%; border: 4px solid var(--white); }
  .quote-name { position: absolute; top: 2025px; width: 331px; text-align: center; font-size: 13px; font-weight: 700; color: var(--accent-dark); letter-spacing: .3px; }

  /* Newsletter + footer */
  .signup-band { position: absolute; left: 0; top: 2105px; width: 1200px; height: 289px; background: var(--band); }
  .signup-form { position: absolute; left: 343px; top: 83px; display: flex; }
  .signup-input { width: 423px; height: 43px; background: var(--white); font-size: 11px; font-weight: 600; color: var(--ink); line-height: 43px; padding-left: 14px; letter-spacing: .3px; }
  .signup-btn { width: 91px; height: 43px; background: var(--accent); color: var(--white); font-size: 13px; font-weight: 700; line-height: 43px; text-align: center; }
  .footer-rule { position: absolute; left: 75px; top: 171px; width: 1052px; height: 1px; background: var(--line); }
  .footer-nav a { position: absolute; top: 203px; font-size: 13px; color: var(--ink-soft); text-decoration: none; letter-spacing: .2px; }
  .copyright { position: absolute; left: 75px; top: 237px; font-size: 11px; color: var(--muted); }
  .follow { position: absolute; left: 970px; top: 217px; font-size: 12px; font-weight: 700; color: var(--ink); }
  .social { position: absolute; top: 212px; width: 22px; height: 22px; border-radius: 3px; background: var(--accent); }
</style>
</head>
<body>

<header class="site-header">
  <div class="brand">
    <span class="brand-mark"></span>
    <span class="brand-name">ROB CARVER</span>
    <span class="brand-tag">HEALTH COACH</span>
  </div>
  <nav class="main-nav">
    <a href="#" class="is-active" style="left:313px">HOME</a>
    <a href="#" style="left:397px">MY PHILOSOPHY</a>
    <a href="#" style="left:549px">INVESTMENT</a>
    <a href="#" style="left:678px">PROJECT YOU</a>
    <a href="#" style="left:814px">EXERCISE SESSIONS</a>
  </nav>
  <a href="#" class="btn-contact">CONTACT &nbsp;ME</a>
</header>

<section class="hero">
  <div class="hero-photo" role="img" aria-label="Photo of a family sharing a picnic meal on a sunny beach by the sea"></div>
  <h1 class="hero-title">ROB CARVER</h1>
  <p class="hero-sub">MEN'S HEALTH COACHING BUSINESS</p>
  <div class="hero-dots"><span class="is-current"></span><span></span><span></span><span></span></div>
  <svg class="hero-curve" viewBox="0 0 1200 40" preserveAspectRatio="none" aria-hidden="true">
    <path d="M0 0 Q600 30 1200 0 L1200 40 L0 40 Z" fill="#ffffff"/>
  </svg>
</section>

<h2 class="section-title" style="top:712px">WHY TO CHOOSE THIS COACHING BUSINESS</h2>
<p class="pillars-lead">Aliquam molestie, mi et imperdiet euismod, dui purus auctor tellus, et interdum lacus lectus et ante.</p>

<!-- Pillar ring template: accent ring with two small gaps -->
<div class="pillar" style="left:196px;top:822px">
  <svg width="92" height="92" viewBox="0 0 92 92" aria-hidden="true">
    <circle cx="46" cy="46" r="43" fill="none" stroke="var(--accent)" stroke-width="2.5" stroke-dasharray="128 7"/>
    <path d="M46 30c3-5 7-6 9-6-1 4-4 6-9 6z" fill="#666"/>
    <path d="M46 34c-6-4-16-2-16 10 0 10 8 18 12 18 2 0 3-1 4-1s2 1 4 1c4 0 12-8 12-18 0-12-10-14-16-10z" fill="#666"/>
    <path d="M39 40l14 14M53 40L39 54" stroke="#fff" stroke-width="2.5"/>
  </svg>
  <span class="pillar-label">NUTRITION</span>
</div>
<div class="pillar" style="left:464px;top:822px">
  <svg width="92" height="92" viewBox="0 0 92 92" aria-hidden="true">
    <circle cx="46" cy="46" r="43" fill="none" stroke="var(--accent)" stroke-width="2.5" stroke-dasharray="128 7"/>
    <rect x="30" y="43" width="32" height="6" rx="2" fill="#666"/>
    <rect x="26" y="35" width="7" height="22" rx="2" fill="#666"/>
    <rect x="59" y="35" width="7" height="22" rx="2" fill="#666"/>
  </svg>
  <span class="pillar-label">EXERCISE</span>
</div>
<div class="pillar" style="left:736px;top:822px">
  <svg width="92" height="92" viewBox="0 0 92 92" aria-hidden="true">
    <circle cx="46" cy="46" r="43" fill="none" stroke="var(--accent)" stroke-width="2.5" stroke-dasharray="128 7"/>
    <path d="M34 64V54c-4-3-6-8-6-13 0-10 8-17 18-17s17 7 17 16l4 7h-4v6c0 2-2 4-4 4h-5v7z" fill="#666"/>
    <circle cx="46" cy="40" r="6" fill="none" stroke="#fff" stroke-width="2.5"/>
  </svg>
  <span class="pillar-label">MENTAL WELL-BEING</span>
</div>
<div class="pillar" style="left:1005px;top:822px">
  <svg width="92" height="92" viewBox="0 0 92 92" aria-hidden="true">
    <circle cx="46" cy="46" r="43" fill="none" stroke="var(--accent)" stroke-width="2.5" stroke-dasharray="128 7"/>
    <path d="M26 36v22M66 46v12M26 52h40" stroke="#666" stroke-width="3" fill="none"/>
    <rect x="29" y="41" width="9" height="7" rx="2" fill="#666"/>
    <rect x="40" y="43" width="26" height="7" rx="2" fill="#666"/>
  </svg>
  <span class="pillar-label">SLEEP - ADEQUATE/QUALITY</span>
</div>
<div class="pillar" style="left:329px;top:988px">
  <svg width="92" height="92" viewBox="0 0 92 92" aria-hidden="true">
    <circle cx="46" cy="46" r="43" fill="none" stroke="var(--accent)" stroke-width="2.5" stroke-dasharray="128 7"/>
    <circle cx="46" cy="46" r="14" fill="#666"/>
    <path d="M32 46h28M46 32c-6 8-6 20 0 28M46 32c6 8 6 20 0 28" stroke="#fff" stroke-width="2" fill="none"/>
  </svg>
  <span class="pillar-label">PLAY - REST AND RECUPERATION</span>
</div>
<div class="pillar" style="left:602px;top:988px">
  <svg width="92" height="92" viewBox="0 0 92 92" aria-hidden="true">
    <circle cx="46" cy="46" r="43" fill="none" stroke="var(--accent)" stroke-width="2.5" stroke-dasharray="128 7"/>
    <circle cx="46" cy="46" r="9" fill="#666"/>
    <g stroke="#666" stroke-width="2.5">
      <path d="M46 27v7M46 58v7M27 46h7M58 46h7M33 33l5 5M54 54l5 5M59 33l-5 5M38 54l-5 5"/>
    </g>
  </svg>
  <span class="pillar-label">SUNLIGHT - ADEQUATE</span>
</div>
<div class="pillar" style="left:871px;top:988px">
  <svg width="92" height="92" viewBox="0 0 92 92" aria-hidden="true">
    <circle cx="46" cy="46" r="43" fill="none" stroke="var(--accent)" stroke-width="2.5" stroke-dasharray="128 7"/>
    <rect x="31" y="28" width="26" height="34" rx="2" fill="none" stroke="#666" stroke-width="2.5"/>
    <path d="M36 36h16M36 42h10" stroke="#666" stroke-width="2"/>
    <circle cx="55" cy="55" r="8" fill="#fff" stroke="#666" stroke-width="2.5"/>
    <path d="M55 51v4l3 2" stroke="#666" stroke-width="2" fill="none"/>
  </svg>
  <span class="pillar-label">PLAN, EXECUTE, REVIEW</span>
</div>

<section class="about">
  <h2 class="section-title" style="top:44px">WHO I AM</h2>
  <div class="about-video" role="img" aria-label="Video still of the coach standing by the sea at dusk">
    <svg class="play-btn" width="60" height="60" viewBox="0 0 60 60" aria-hidden="true">
      <circle cx="30" cy="30" r="27" fill="none" stroke="#fff" stroke-width="5"/>
      <path d="M24 18l18 12-18 12z" fill="#fff"/>
    </svg>
  </div>
</section>

<h2 class="section-title" style="top:1715px">TESTIMONIALS</h2>

<blockquote class="quote-card" style="left:75px">" Aliquam molestie, mi et imperdiet euismod, dui purus auctor tellus, et interdum lacus lectus et ante. Sed accumsan sollicitudin sapien, sit amet adipiscing turpis gravida egestas risus in magna.."</blockquote>
<blockquote class="quote-card" style="left:435px">" Aliquam molestie, mi et imperdiet euismod, dui purus auctor tellus, et interdum lacus lectus et ante. Sed accumsan sollicitudin sapien, sit amet adipiscing turpis gravida egestas risus in magna.."</blockquote>
<blockquote class="quote-card" style="left:796px">" Aliquam molestie, mi et imperdiet euismod, dui purus auctor tellus, et interdum lacus lectus et ante. Sed accumsan sollicitudin sapien, sit amet adipiscing turpis gravida egestas risus in magna.."</blockquote>

<div class="quote-avatar" style="left:194px;background:linear-gradient(160deg,#d9d9d9,#7a7f86)" role="img" aria-label="Portrait of a client in a suit"></div>
<div class="quote-avatar" style="left:554px;background:linear-gradient(160deg,#e4e4e4,#8c8c8c)" role="img" aria-label="Portrait of an older client with glasses"></div>
<div class="quote-avatar" style="left:915px;background:linear-gradient(160deg,#c9b79a,#6e6a5e)" role="img" aria-label="Portrait of a client wearing a hat"></div>

<p class="quote-name" style="left:75px">NAME HEADING</p>
<p class="quote-name" style="left:435px">NAME HEADING</p>
<p class="quote-name" style="left:796px">NAME HEADING</p>

<footer class="signup-band">
  <h2 class="section-title" style="top:37px;font-size:19px">JOIN E-MAIL LISTING</h2>
  <div class="signup-form">
    <div class="signup-input">ENTER EMAIL ADDRESS</div>
    <div class="signup-btn">SIGN UP</div>
  </div>
  <div class="footer-rule"></div>
  <nav class="footer-nav">
    <a href="#" style="left:75px">HOME</a>
    <a href="#" style="left:151px">MY PHILOSOPHY</a>
    <a href="#" style="left:294px">INVESTMENT</a>
    <a href="#" style="left:415px">PROJECT YOU</a>
    <a href="#" style="left:541px">EXERCISE SESSIONS</a>
    <a href="#" style="left:708px">CONTACT ME</a>
  </nav>
  <p class="copyright">Copyright © 2017. Company Name. &nbsp;All Right Reserved</p>
  <span class="follow">FOLLOW ME</span>
  <span class="social" style="left:1060px" role="img" aria-label="Social profile link"></span>
  <span class="social" style="left:1105px" role="img" aria-label="Professional network link"></span>
</footer>

</body>
</html>
```